New hardcover book cover

I want a striking, eye-catching cover with title, subtitle and a picture.See for previous book covers: www.brightmaplepress.com

Target Market(s)

young, successful entrepreneurs that have built a business in a niche market that they discovered.

Font styles to use
Serif

Colors

Designer to choose colors to be used in the design.

Requirements
Must have
• A book cover that impresses and captures the imagination of those who look at it.
• MY MISTAKE, SORRY.
• Title: Founders Behind the Quiet Trade Boom
• Subtitle: 25 stories of success from
• discovering hidden opportunities
• Author: Dorian Pelham
• Please use the photo attached, thanks.

```html
<!DOCTYPE html>
<html lang="en">
<head>
<meta charset="utf-8">
<title>Founders Behind the Quiet Trade Boom — Dorian Pelham</title>
<link href="https://fonts.googleapis.com/css2?family=Teko:wght@600&family=Josefin+Sans:wght@300;400&display=swap" rel="stylesheet">
<style>
  :root {
    --stage: #2a2a2a;
    --cover: #e3e3e1;
    --title-red: #c6231b;
    --subtitle-grey: #5a5a5a;
    --board-dark: #4a4a4a;
    --board-mid: #8a8a8a;
    --board-light: #bdbdbd;
    --dart-dark: #5c5c5c;
    --dart-light: #a4a4a4;
  }
  * { margin: 0; padding: 0; box-sizing: border-box; }
  html, body {
    width: 1200px;
    height: 905px;
    overflow: hidden;
    background: var(--stage);
  }
  .stage {
    position: relative;
    width: 1200px;
    height: 905px;
  }
  .book-cover {
    position: absolute;
    left: 320px;
    top: 22px;
    width: 560px;
    height: 860px;
    background: var(--cover);
    overflow: hidden;
  }
  .cover-photo {
    position: absolute;
    left: 0;
    top: 0;
    width: 560px;
    height: 860px;
    display: block;
  }
  .title {
    position: absolute;
    left: 155px;
    top: 96px;
    color: var(--title-red);
    font-family: "Teko", "Arial Narrow", sans-serif;
    font-weight: 600;
    text-transform: uppercase;
    line-height: 0.86;
  }
  .title-line { display: block; }
  .title-founders { font-size: 64px; letter-spacing: 0.5px; }
  .title-row { display: flex; align-items: flex-end; gap: 8px; }
  .title-small {
    display: flex;
    flex-direction: column;
    font-size: 27px;
    line-height: 0.82;
    padding-bottom: 8px;
    text-align: center;
  }
  .title-quiet { font-size: 92px; }
  .title-trade { font-size: 92px; }
  .title-boom { font-size: 124px; }
  .subtitle {
    position: absolute;
    left: 155px;
    top: 596px;
    width: 360px;
    color: var(--subtitle-grey);
    font-family: "Josefin Sans", "Helvetica", sans-serif;
    font-weight: 400;
    font-size: 19px;
    letter-spacing: 1.5px;
    line-height: 1.35;
    text-transform: uppercase;
  }
  .author {
    position: absolute;
    left: 222px;
    top: 730px;
    color: var(--title-red);
    font-family: "Josefin Sans", "Helvetica", sans-serif;
    font-weight: 300;
    font-size: 34px;
    letter-spacing: 4px;
    line-height: 1.12;
    text-transform: uppercase;
  }
</style>
</head>
<body>
  <main class="stage">
    <section class="book-cover">
      <svg class="cover-photo" role="img" aria-label="Black and white photo of a dartboard seen edge-on along the left side, with a dart striking the bullseye and its flight reaching into the cover" viewBox="0 0 560 860">
        <defs>
          <linearGradient id="board-tone" x1="0" y1="0" x2="1" y2="0">
            <stop offset="0" stop-color="var(--board-dark)"/>
            <stop offset="0.55" stop-color="var(--board-mid)"/>
            <stop offset="1" stop-color="var(--board-light)"/>
          </linearGradient>
          <linearGradient id="dart-tone" x1="0" y1="0" x2="1" y2="0">
            <stop offset="0" stop-color="var(--dart-dark)"/>
            <stop offset="1" stop-color="var(--dart-light)"/>
          </linearGradient>
        </defs>
        <rect class="board-area" width="118" height="860" fill="url(#board-tone)"/>
        <rect class="dart-area" x="118" y="440" width="310" height="100" rx="10" fill="url(#dart-tone)" opacity="0.55"/>
      </svg>

      <h1 class="title">
        <span class="title-line title-founders">Founders</span>
        <span class="title-line title-row">
          <span class="title-small"><span>Behind</span><span>the</span></span>
          <span class="title-quiet">Quiet</span>
        </span>
        <span class="title-line title-trade">Trade</span>
        <span class="title-line title-boom">Boom</span>
      </h1>

      <p class="subtitle">25 stories of success from discovering hidden opportunities</p>

      <p class="author">Dorian<br>Pelham</p>
    </section>
  </main>
</body>
</html>
```